Business cards, ppt template and stationnary for flying robotics startup Skorvent
Skorvent
Business cards, ppt template and stationnary for flying robotics startup Skorvent - Engineering
Creative Brief
Professional
Marcel Dujoux
Co-founder - Head of Business Development
Skorvent SA Orbanne Science Park Building D 1027 Veyrenne Switzerland
mdujoux@skorvent-mail.example
www.skorvent-web.example
we need business cards in European format [85mm/3.346in x 55mm/2.165in], powerpoint templates and stationnary (A4 format).

```html
<!DOCTYPE html>
<html lang="en">
<head>
<meta charset="utf-8">
<title>Skorvent stationery and presentation template</title>
<link rel="stylesheet" href="https://fonts.googleapis.com/css2?family=Open+Sans:wght@400;600;700&family=Montserrat:wght@600;700;800&display=swap">
<style>
:root{
  --red:#e3232b;
  --red-dark:#b8161d;
  --ink:#333;
  --muted:#8a8a8a;
  --line:#d6d6d6;
  --paper:#fff;
  --canvas:#e7e7e7;
  --soft:#f1f1f1;
}
*{box-sizing:border-box;margin:0;padding:0}
html,body{width:1200px;height:372px;overflow:hidden;background:var(--canvas);font-family:"Open Sans",sans-serif;color:var(--ink)}
.board{position:relative;width:1200px;height:372px}
.sheet{position:absolute;background:var(--paper);box-shadow:0 1px 4px rgba(0,0,0,.25);overflow:hidden}
.brand{display:flex;align-items:center;gap:4px;font-family:"Montserrat",sans-serif;font-weight:700;color:var(--red);letter-spacing:.5px;text-transform:uppercase;white-space:nowrap}
.brand-dot{border-radius:50%;background:var(--red);flex:none}
.brand.light{color:#fff}.brand.light .brand-dot{background:#fff}
.tiny{font-size:4px;line-height:6px;color:var(--muted)}
.foot-band{position:absolute;left:0;right:0;bottom:0}

/* business cards */
.card-front{left:17px;top:19px;width:134px;height:86px}
.card-front .brand{position:absolute;left:0;right:0;top:30px;justify-content:center;font-size:11px}
.card-front .brand-dot{width:12px;height:12px}
.card-back{left:17px;top:112px;width:134px;height:86px}
.card-back .brand{position:absolute;left:10px;top:10px;font-size:7px}
.card-back .brand-dot{width:8px;height:8px}
.person{position:absolute;left:10px;top:32px}
.person-name{font-size:6.5px;font-weight:700;color:var(--red)}
.person-role{font-size:4px;color:var(--muted);line-height:6px}
.card-contact{position:absolute;left:10px;top:50px;right:8px}
.card-web{position:absolute;right:8px;bottom:3px;font-size:4px;color:#fff;z-index:2}

/* letterhead */
.letter{left:163px;top:19px;width:196px;height:280px}
.letter .brand{position:absolute;left:14px;top:16px;font-size:9px}
.letter .brand-dot{width:10px;height:10px}
.letter-sender{position:absolute;right:14px;top:14px;text-align:right}
.letter-recipient{position:absolute;left:14px;top:48px}
.letter-body{position:absolute;left:14px;right:14px;top:88px}
.letter-body p{margin-bottom:4px}
.letter-sign{position:absolute;left:14px;top:190px}
.sign-line{display:block;width:50px;height:12px}

/* envelope */
.envelope{left:17px;top:230px;width:138px;height:130px}
.envelope .brand{position:absolute;left:0;right:0;top:10px;justify-content:center;font-size:7px}
.envelope .brand-dot{width:8px;height:8px}
.envelope-address{position:absolute;left:70px;top:72px}

/* slides */
.slide{width:197px;height:152px}
.s1{left:376px;top:19px}.s2{left:581px;top:19px}.s3{left:786px;top:19px}.s4{left:991px;top:19px}
.s5{left:376px;top:190px}.s6{left:581px;top:190px}.s7{left:786px;top:190px}.s8{left:991px;top:190px}
.slide .brand{position:absolute;right:10px;top:8px;font-size:7px}
.slide .brand-dot{width:8px;height:8px}
.slide-title{position:absolute;left:12px;top:22px;font-family:"Montserrat",sans-serif;font-weight:700;font-size:9px;color:var(--red);text-transform:uppercase;white-space:nowrap}
.slide-sub{position:absolute;left:12px;top:33px;font-size:4px;color:var(--muted);text-transform:uppercase;letter-spacing:.3px}
.deck-name{position:absolute;left:12px;top:64px;font-family:"Montserrat",sans-serif;font-weight:800;font-size:14px;color:var(--red);text-transform:uppercase;white-space:nowrap}
.deck-title{position:absolute;left:12px;top:82px;font-size:6px;font-weight:600;color:var(--ink);text-transform:uppercase}
.slide-text{position:absolute;left:12px;top:44px;width:90px}
.photo-slot{position:absolute;background:linear-gradient(135deg,#d9d9d9,#bdbdbd)}
.pie{position:absolute;right:14px;top:46px;width:70px;height:70px}
.bars{position:absolute;left:70px;top:46px;width:110px;height:82px}
.groups{position:absolute;left:12px;top:46px;right:12px;display:grid;grid-template-columns:1fr 1fr;gap:6px 10px}
.group-name{font-size:5px;font-weight:700;color:var(--red)}
.thanks{background:var(--red)}
.thanks .brand{position:absolute;left:0;right:0;top:38px;justify-content:center;font-size:11px}
.thanks .brand-dot{width:12px;height:12px}
.thanks-title{position:absolute;left:0;right:0;top:92px;text-align:center;font-family:"Montserrat",sans-serif;font-weight:800;font-size:12px;color:#fff;text-transform:uppercase}
.thanks-sub{position:absolute;left:0;right:0;top:108px;text-align:center;font-size:5px;color:#fff;text-transform:uppercase;letter-spacing:.4px}
</style>
</head>
<body>
<main class="board">

  <section class="sheet card-front">
    <div class="brand"><span class="brand-dot"></span>Skorvent</div>
    <svg class="foot-band" width="134" height="14" viewBox="0 0 134 14"><path d="M0 14 L0 8 Q67 -2 134 6 L134 14Z" fill="var(--red)"/></svg>
  </section>

  <section class="sheet card-back">
    <div class="brand"><span class="brand-dot"></span>Skorvent</div>
    <div class="person">
      <div class="person-name">Marcel Dujoux</div>
      <div class="person-role">Co-founder - Head of Business Development</div>
    </div>
    <div class="card-contact tiny">
      Skorvent SA, Orbanne Science Park Building D<br>
      1027 Veyrenne, Switzerland<br>
      mdujoux@skorvent-mail.example
    </div>
    <svg class="foot-band" width="134" height="12" viewBox="0 0 134 12"><path d="M0 12 L0 6 Q67 -2 134 5 L134 12Z" fill="var(--red)"/></svg>
    <div class="card-web">www.skorvent-web.example</div>
  </section>

  <section class="sheet letter">
    <div class="brand"><span class="brand-dot"></span>Skorvent</div>
    <div class="letter-sender tiny">Skorvent SA<br>Orbanne Science Park<br>Building D<br>1027 Veyrenne, Switzerland</div>
    <div class="letter-recipient tiny">Mr. Recipient Name<br>Company Name Ltd<br>Street Address 12<br>1000 City</div>
    <div class="letter-body tiny">
      <p>Dear Sir or Madam,</p>
      <p>Thank you for your recent message. We are pleased to send you the information you requested and look forward to working with you.</p>
      <p>Our team would be glad to arrange a short meeting at a time that suits you, and to answer any question you may have.</p>
      <p>Please do not hesitate to contact us with any further questions.</p>
    </div>
    <div class="letter-sign tiny">
      <p>Best regards,</p>
      <svg class="sign-line" viewBox="0 0 50 12"><path d="M2 9 C8 1 12 11 18 5 S28 9 34 4 S44 8 48 6" fill="none" stroke="var(--ink)" stroke-width=".8"/></svg>
      <p>Marcel Dujoux</p>
    </div>
    <svg class="foot-band" width="196" height="16" viewBox="0 0 196 16"><path d="M0 16 L0 10 Q98 -2 196 8 L196 16Z" fill="var(--red)"/></svg>
  </section>

  <section class="sheet envelope">
    <svg width="138" height="130" viewBox="0 0 138 130" style="position:absolute;left:0;top:0">
      <path d="M0 0 H138 V18 Q69 56 0 18Z" fill="var(--red)"/>
      <path d="M0 130 L0 121 Q69 110 138 119 L138 130Z" fill="var(--red)"/>
    </svg>
    <div class="brand light"><span class="brand-dot"></span>Skorvent</div>
    <div class="envelope-address tiny">Recipient Name<br>Street Address 12<br>1000 City</div>
  </section>

  <section class="sheet slide s1">
    <svg width="197" height="152" viewBox="0 0 197 152" style="position:absolute;left:0;top:0">
      <path d="M197 20 Q120 60 150 152 L197 152Z" fill="var(--soft)"/>
      <path d="M0 152 L0 130 Q100 104 197 122 L197 152Z" fill="var(--red)"/>
    </svg>
    <div class="brand"><span class="brand-dot"></span>Skorvent</div>
    <div class="deck-name">Presentation Name</div>
    <div class="deck-title">Presentation Title</div>
  </section>

  <section class="sheet slide s2">
    <div class="brand"><span class="brand-dot"></span>Skorvent</div>
    <div class="slide-title">Presentation Heading</div>
    <div class="slide-sub">Subtitle goes here</div>
    <div class="slide-text tiny">Lorem ipsum dolor sit amet, consectetur adipiscing elit. Sed do eiusmod tempor incididunt ut labore et dolore magna aliqua.</div>
    <div class="photo-slot" style="left:108px;top:44px;width:77px;height:80px" role="img" aria-label="Product photo placeholder"></div>
    <svg class="foot-band" width="197" height="10" viewBox="0 0 197 10"><rect width="197" height="10" fill="var(--red)"/></svg>
  </section>

  <section class="sheet slide s3">
    <div class="brand"><span class="brand-dot"></span>Skorvent</div>
    <div class="slide-title">Lorem Ipsum</div>
    <div class="photo-slot" style="left:12px;top:40px;width:100px;height:84px" role="img" aria-label="Product photo placeholder"></div>
    <div class="tiny" style="position:absolute;left:120px;top:40px;width:66px">Lorem ipsum dolor sit amet, consectetur adipiscing elit, sed do eiusmod tempor.</div>
    <svg class="foot-band" width="197" height="10" viewBox="0 0 197 10"><rect width="197" height="10" fill="var(--red)"/></svg>
  </section>

  <section class="sheet slide s4">
    <div class="brand"><span class="brand-dot"></span>Skorvent</div>
    <div class="slide-title">Presentation Heading</div>
    <div class="slide-sub">Subtitle goes here</div>
    <div class="slide-text tiny" style="width:92px">Lorem ipsum dolor sit amet, consectetur adipiscing elit sed do eiusmod.</div>
    <svg class="pie" viewBox="0 0 70 70">
      <circle cx="35" cy="35" r="33" fill="#555"/>
      <path d="M35 35 L35 2 A33 33 0 0 1 66 46Z" fill="var(--red)"/>
      <path d="M35 35 L66 46 A33 33 0 0 1 30 68Z" fill="#bdbdbd"/>
    </svg>
    <svg class="foot-band" width="197" height="10" viewBox="0 0 197 10"><rect width="197" height="10" fill="var(--red)"/></svg>
  </section>

  <section class="sheet slide s5">
    <div class="brand"><span class="brand-dot"></span>Skorvent</div>
    <div class="slide-title">Lorem Ipsum</div>
    <div class="slide-sub">Subtitle goes here</div>
    <div class="slide-text tiny" style="width:52px">Lorem ipsum dolor sit amet, consectetur elit.</div>
    <svg class="bars" viewBox="0 0 110 82">
      <line x1="4" y1="0" x2="4" y2="80" stroke="var(--line)"/>
      <rect x="4" y="6" width="70" height="8" fill="var(--red)"/>
      <rect x="4" y="22" width="50" height="8" fill="var(--red)"/>
      <rect x="4" y="38" width="86" height="8" fill="var(--red)"/>
      <rect x="4" y="54" width="36" height="8" fill="var(--red)"/>
      <rect x="4" y="70" width="60" height="8" fill="#9a9a9a"/>
    </svg>
    <svg class="foot-band" width="197" height="10" viewBox="0 0 197 10"><rect width="197" height="10" fill="var(--red)"/></svg>
  </section>

  <section class="sheet slide s6">
    <div class="brand"><span class="brand-dot"></span>Skorvent</div>
    <div class="slide-title">Presentation Heading</div>
    <div class="slide-sub">Subtitle goes here</div>
    <div class="groups">
      <div><div class="group-name">Group 1</div><div class="tiny">Lorem ipsum dolor sit amet elit.</div></div>
      <div><div class="group-name">Group 2</div><div class="tiny">Lorem ipsum dolor sit amet elit.</div></div>
      <div><div class="group-name">Group 3</div><div class="tiny">Lorem ipsum dolor sit amet elit.</div></div>
      <div><div class="group-name">Group 4</div><div class="tiny">Lorem ipsum dolor sit amet elit.</div></div>
    </div>
    <svg class="foot-band" width="197" height="10" viewBox="0 0 197 10"><rect width="197" height="10" fill="var(--red)"/></svg>
  </section>

  <section class="sheet slide s7">
    <div class="brand"><span class="brand-dot"></span>Skorvent</div>
    <div class="slide-title">Presentation Heading</div>
    <div class="slide-sub">Subtitle goes here</div>
    <div class="groups" style="right:80px;grid-template-columns:1fr">
      <div><div class="group-name">Group 1</div><div class="tiny">Lorem ipsum dolor sit amet.</div></div>
      <div><div class="group-name">Group 2</div><div class="tiny">Lorem ipsum dolor sit amet.</div></div>
      <div><div class="group-name">Group 3</div><div class="tiny">Lorem ipsum dolor sit amet.</div></div>
    </div>
    <div class="photo-slot" style="left:124px;top:46px;width:61px;height:80px" role="img" aria-label="Photo placeholder"></div>
    <svg class="foot-band" width="197" height="10" viewBox="0 0 197 10"><rect width="197" height="10" fill="var(--red)"/></svg>
  </section>

  <section class="sheet slide s8 thanks">
    <svg width="197" height="152" viewBox="0 0 197 152" style="position:absolute;left:0;top:0">
      <path d="M0 152 L0 128 Q100 104 197 124 L197 152Z" fill="var(--red-dark)"/>
    </svg>
    <div class="brand light"><span class="brand-dot"></span>Skorvent</div>
    <div class="thanks-title">Thank you so much!</div>
    <div class="thanks-sub">Presentation Name</div>
  </section>

</main>
</body>
</html>
```